Revise our Visual Graphic - CPA firm

We are a small specialty CPA firm that provides consulting services to companies in three areas: Information Security, Compliance & Attestation.

We need a tool to present our range of services and how they help our customers. We might use this on the website and when meeting face to face with clients to talk through what we do and how we can help.

I'm seeking a revised and updated graphic presentation image to explain our services. This graphic framework image will be one we can use on our website and use when we sell and explain our services to our clients. This graphic framework is meant to be a visual tool to make is easier to explain what we do to our clients.

We have a graphic that we like, but we don't LOVE IT yet. Your mission is you choose to accept it is to professionalize our graphic design. (see attached graphic)

The overall "environment" is represented by RISK, REGULATORY, REVENUE. These are the 3 reasons people would hire us. The bigger picture eco system.

The three overlapping circles show are three major service categories and inside the circles are lists of the specific services we can provide. We have overlapping circles to show that we can save them money and time if we provide more than one type of service.

The words on the dotted lines are what we commonly do on each project which is 3 things: IDENTIFY, EVALUATE, REPORT. These three things we do for all of our services so a faint circle with arrows or somehow showing a circular ongoing process would be good.

As you can see we are using one graphic to show many things and relationships.

The title of this graphic is "K7 Framework"

I look forward to your great ideas! Thanks.

Reason: Just to give a little more time after the weekend.

Target Market(s)

Presidents and Vice Presidents of small companies.

Industry/Entity Type

Graphic Design

Colors
faee3f
86cfc7
acd037
f68d4d

Requirements
Must have
• Be able to show this visual on one page of a website or PowerPoint presentation without scrolling down.

All of the written text on my draft example must be used and fit into the new design.
Nice to have
• When you design it think of how this can be used for both presentations, but also may be used on the website and people might click on different elements to learn more.

I picked some colors, but feel free to pick other colors. The only important thing to know is that the logo is black and yellow.

```html
<!DOCTYPE html>
<html lang="en">
<head>
<meta charset="utf-8">
<title>K7 Framework</title>
<link href="https://fonts.googleapis.com/css2?family=Arimo:wght@700&family=Nunito:wght@900&display=swap" rel="stylesheet">
<style>
  :root {
    --navy: #2e3192;
    --signal-red: #e31e24;
    --triangle-peach: #f8b88b;
    --ring-magenta: #c8559f;
    --ring-edge: #b0428a;
    --core-cream: #fde4cd;
    --brand-pink: #e4197f;
    --cycle-orange: #f7901e;
    --cycle-red: #e8242b;
    --cycle-blue: #2e4a9e;
    --ink: #111111;
    --white: #ffffff;
  }
  html, body {
    margin: 0;
    padding: 0;
    overflow: hidden;
    background: var(--white);
  }
  .framework-canvas {
    width: 1200px;
    height: 1004px;
    position: relative;
    overflow: hidden;
    background: var(--white);
  }
  .framework-art {
    display: block;
    width: 1200px;
    height: 1004px;
  }
  .title-text {
    font-family: "Nunito", sans-serif;
    font-weight: 900;
    font-size: 74px;
    fill: var(--navy);
  }
  .driver-label {
    font-family: "Arimo", sans-serif;
    font-weight: 700;
    font-size: 46px;
    fill: var(--signal-red);
  }
  .ring-label {
    font-family: "Arimo", sans-serif;
    font-weight: 700;
    font-size: 27px;
    letter-spacing: 1px;
    fill: var(--white);
  }
  .service-list {
    font-family: "Arimo", sans-serif;
    font-weight: 700;
    font-size: 19px;
    fill: var(--white);
  }
  .step-label {
    font-family: "Arimo", sans-serif;
    font-weight: 700;
    font-size: 27px;
    fill: var(--ink);
  }
  .brand-name {
    font-family: "Arimo", sans-serif;
    font-weight: 700;
    font-size: 56px;
    fill: var(--brand-pink);
  }
</style>
</head>
<body>
<main class="framework-canvas">
  <svg class="framework-art" viewBox="0 0 1200 1004" xmlns="http://www.w3.org/2000/svg" aria-labelledby="framework-title">
    <title id="framework-title">K7 Framework: Regulatory, Risk and Revenue around Information Security, Compliance and Attestation</title>
    <defs>
      <linearGradient id="cycle-fill" x1="0" y1="0" x2="1" y2="1">
        <stop offset="0" stop-color="var(--cycle-orange)"/>
        <stop offset="0.5" stop-color="var(--cycle-red)"/>
        <stop offset="1" stop-color="var(--cycle-blue)"/>
      </linearGradient>
      <path id="title-arc" d="M 290 165 Q 600 15 910 165"/>
      <path id="arc-information-security" d="M 325.6 460.1 A 292 292 0 0 1 874.4 460.1"/>
      <path id="arc-compliance" d="M 524.4 842.1 A 292 292 0 0 1 393.5 353.5"/>
      <path id="arc-attestation" d="M 806.5 353.5 A 292 292 0 0 1 675.6 842.1"/>
    </defs>

    <text class="title-text" text-anchor="middle">
      <textPath href="#title-arc" startOffset="50%">K7 Framework</textPath>
    </text>

    <polygon class="environment-triangle" points="600,150 95,915 1105,915" fill="var(--triangle-peach)"/>

    <text class="driver-label driver-regulatory" x="600" y="216" text-anchor="middle">REGULATORY</text>
    <text class="driver-label driver-risk" x="330" y="882" text-anchor="middle">RISK</text>
    <text class="driver-label driver-revenue" x="935" y="882" text-anchor="middle">REVENUE</text>

    <circle class="service-ring" cx="600" cy="560" r="330" fill="var(--ring-magenta)" stroke="var(--ring-edge)" stroke-width="3"/>
    <circle class="service-core" cx="600" cy="560" r="275" fill="var(--core-cream)" stroke="var(--ring-edge)" stroke-width="2"/>

    <text class="ring-label" text-anchor="middle">
      <textPath href="#arc-information-security" startOffset="50%">INFORMATION SECURITY</textPath>
    </text>
    <text class="ring-label" text-anchor="middle">
      <textPath href="#arc-compliance" startOffset="50%">COMPLIANCE</textPath>
    </text>
    <text class="ring-label" text-anchor="middle">
      <textPath href="#arc-attestation" startOffset="50%">ATTESTATION</textPath>
    </text>

    <path class="process-cycle" role="img" aria-label="Illustration of a continuous cycle of three arrows: Identify, Evaluate, Report"
      fill="url(#cycle-fill)" fill-rule="evenodd"
      d="M 840 560 A 240 240 0 1 1 360 560 A 240 240 0 1 1 840 560 Z M 740 560 A 140 140 0 1 0 460 560 A 140 140 0 1 0 740 560 Z"/>

    <text class="service-list list-information-security">
      <tspan x="655" y="360">ISO 27001</tspan>
      <tspan x="655" y="383">PCI-DSS</tspan>
      <tspan x="655" y="406">Penetration</tspan>
      <tspan x="655" y="429">Test</tspan>
    </text>
    <text class="service-list list-attestation">
      <tspan x="690" y="686">SSAE 16</tspan>
      <tspan x="690" y="710">NetAssure</tspan>
      <tspan x="690" y="734">SOC 2</tspan>
    </text>
    <text class="service-list list-compliance" text-anchor="middle">
      <tspan x="414" y="440">CFPB</tspan>
      <tspan x="414" y="464">Readiness</tspan>
      <tspan x="414" y="488">FISMA</tspan>
      <tspan x="414" y="512">FedRamp</tspan>
      <tspan x="414" y="536">HITECH</tspan>
      <tspan x="414" y="560">HIPAA</tspan>
    </text>

    <text class="step-label step-identify" transform="translate(516 430) rotate(52)" text-anchor="middle">Identify</text>
    <text class="step-label step-evaluate" x="760" y="552" text-anchor="middle">Evaluate</text>
    <text class="step-label step-report" transform="translate(520 712) rotate(-52)" text-anchor="middle">Report</text>

    <text class="brand-name" x="600" y="596" text-anchor="middle">Veritrue</text>
  </svg>
</main>
</body>
</html>
```